I have a basic design of a poster that I want to make look better. The poster is a list of continuing medical education rules.

JRPPS = Joint Registry for Postgraduate Physician Studies This text should be included. You might also want to include "CME". Please use all the existing elements in the file.

I want to sell this poster to CME offices around the US. The poster should be 24 by 36

Reason: I would like to see more designs. I have received less than ten.

Target Market(s)

CME professionals

Industry/Entity Type

Medical

Colors

Designer to choose colors to be used in the design.

Requirements
Must have
• All elements in the file provided. You can also spell out Joint Registry for Postgraduate Physician Studies.

```html
<!DOCTYPE html>
<html lang="en">
<head>
<meta charset="utf-8">
<title>JRPPS Accreditation Criteria</title>
<link rel="stylesheet" href="https://fonts.googleapis.com/css2?family=Open+Sans:wght@400;700;800&family=Varela+Round&family=Arimo:wght@400&display=swap">
<style>
:root{
  --slate:#476a86;
  --slate-dark:#3b5a74;
  --parchment:#e6dcc0;
  --gold:#d8bf82;
  --card:#d7be87;
  --crimson:#7b1b20;
  --ink:#1f1f1f;
  --cream:#f4ecd9;
}
*{box-sizing:border-box;margin:0;padding:0}
html,body{width:800px;height:1200px;overflow:hidden;background:var(--slate)}
.poster{position:relative;width:800px;height:1200px;background:var(--slate);font-family:"Arimo",Arial,sans-serif;color:var(--ink)}
.title-band{position:absolute;left:22px;top:18px;width:756px;height:52px;background:var(--gold);display:flex;align-items:center;padding-left:64px}
.title-band h1{font-family:"Open Sans",Arial,sans-serif;font-weight:800;font-size:29px;color:var(--slate-dark);letter-spacing:.2px}
.panel{position:absolute;left:22px;width:756px;background:var(--parchment)}
.panel-criteria{top:74px;height:690px}
.panel-commendation{top:770px;height:410px}
.section-head{position:absolute;left:0;right:0;display:flex;align-items:center;height:28px}
.section-head .bar{height:12px;background:var(--slate)}
.section-head .bar.lead{width:48px}
.section-head .bar.tail{flex:1}
.section-head h2{font-family:"Open Sans",Arial,sans-serif;font-weight:400;font-size:21px;color:var(--slate-dark);padding:0 10px;letter-spacing:.3px;white-space:nowrap}
.intro{position:absolute;left:20px;top:32px;width:722px;font-size:10.2px;line-height:1.38}
.grid{position:absolute;left:11px;display:grid;grid-template-columns:235px 235px 235px;column-gap:14px}
.grid-criteria{top:83px;grid-template-rows:repeat(5,111px);row-gap:11px}
.grid-commendation{top:45px;grid-template-rows:repeat(3,111px);row-gap:12px}
.criterion{display:flex;flex-direction:column;background:var(--card)}
.criterion h3{height:31px;background:var(--crimson);color:var(--cream);font-family:"Varela Round",Arial,sans-serif;font-weight:400;font-size:19px;text-align:center;line-height:31px}
.criterion p{padding:8px 11px;font-size:10.4px;line-height:1.38;text-align:justify}
.criterion.retired p{padding:24px 14px;font-size:12px;text-align:left}
.criterion.dense p{font-size:9.6px;line-height:1.36}
.site{position:absolute;right:38px;bottom:24px;font-family:"Open Sans",Arial,sans-serif;font-size:15px;color:var(--ink)}
</style>
</head>
<body>
<main class="poster">
  <header class="title-band"><h1>JRPPS Accreditation Criteria</h1></header>

  <section class="panel panel-criteria">
    <div class="section-head" style="top:2px"><span class="bar lead"></span><h2>ACCREDITATION CRITERIA</h2><span class="bar tail"></span></div>
    <p class="intro">The Accreditation Criteria are divided into three levels. To achieve Provisional Accreditation, a two year term, providers must comply with Criteria 1, 2, 3, and 7–12. Providers seeking full Accreditation or reaccreditation for a four-year term must comply with Criteria 1–13. To achieve Accreditation with Commendation, a six-year term, providers must comply with all Accreditation Criteria</p>
    <div class="grid grid-criteria">
      <article class="criterion"><h3>Criterion 1</h3><p>The provider has a CME mission statement that includes expected results articulated in terms of in competence, performance, or patient outcomes that will be the result of the program.</p></article>
      <article class="criterion"><h3>Criterion 2</h3><p>The provider incorporates into CME activities the educational needs (knowledge, competence, or performance) that underlie the professional practice gaps of their own learners.</p></article>
      <article class="criterion"><h3>Criterion 3</h3><p>The provider generates activities/educational interventions that are designed to change competence, performance, or patient outcomes as described in its mission statement.</p></article>
      <article class="criterion retired"><h3>Criterion 4</h3><p>This criterion has been eliminated effective February 2014.</p></article>
      <article class="criterion"><h3>Criterion 5</h3><p>The provider chooses educational formats for activities/interventions that are appropriate for the setting, objectives, and desired results of the activity.</p></article>
      <article class="criterion dense"><h3>Criterion 6</h3><p>The provider develops activities/educational interventions in the context of desirable physician attributes [eg, National Clinical Practice Institute (NCPI) competencies, Graduate Physician Training Board (GPTB) Competencies].</p></article>
      <article class="criterion"><h3>Criterion 7</h3><p>The provider develops activities/ educational interventions independent of commercial interests. (SCS 1, 2, and 6).</p></article>
      <article class="criterion"><h3>Criterion 8</h3><p>The provider appropriately manages commercial support (if applicable, SCS 3 of the JRPPS Standards for Commercial Support).</p></article>
      <article class="criterion"><h3>Criterion 9</h3><p>The provider maintains a separation of promotion from education (SCS 4).</p></article>
      <article class="criterion"><h3>Criterion 10</h3><p>The provider actively promotes improvements in health care and NOT proprietary interests of a commercial interest (SCS 5).</p></article>
      <article class="criterion"><h3>Criterion 11</h3><p>The provider analyzes changes in learners (competence, performance, or patient outcomes) achieved as a result of the overall program's activities/educational interventions.</p></article>
      <article class="criterion"><h3>Criterion 12</h3><p>The provider gathers data or information and conducts a program-based analysis on the degree to which the CME mission of the provider has been met through the conduct of CME activities/educational interventions.</p></article>
      <article class="criterion dense"><h3>Criterion 13</h3><p>The provider identifies, plans and implements the needed or desired changes in the overall program (eg, planners, teachers, infrastructure, methods, resources, facilities, interventions) that are required to improve on ability to meet the CME mission.</p></article>
      <article class="criterion retired"><h3>Criterion 14</h3><p>This criterion has been eliminated effective February 2014.</p></article>
      <article class="criterion retired"><h3>Criterion 15</h3><p>This criterion has been eliminated effective February 2014.</p></article>
    </div>
  </section>

  <section class="panel panel-commendation">
    <div class="section-head" style="top:4px"><span class="bar lead"></span><h2>ACCREDITATION WITH COMMENDATION</h2><span class="bar tail"></span></div>
    <div class="grid grid-commendation">
      <article class="criterion"><h3>Criterion 16</h3><p>The provider operates in a manner that integrates CME into the process for improving professional practice.</p></article>
      <article class="criterion"><h3>Criterion 17</h3><p>The provider utilizes non-education strategies to enhance change as an adjunct to its activities / educational interventions (e.g., reminders, patient feedback).</p></article>
      <article class="criterion"><h3>Criterion 18</h3><p>The provider identifies factors outside the provider's control that impact on patient outcomes.</p></article>
      <article class="criterion"><h3>Criterion 19</h3><p>The provider implements educational strategies to remove, overcome or address barriers to physician change.</p></article>
      <article class="criterion"><h3>Criterion 20</h3><p>The provider builds bridges with other stakeholders through collaboration and cooperation.</p></article>
      <article class="criterion"><h3>Criterion 21</h3><p>The provider participates within an institutional or system framework for quality improvement.</p></article>
      <article class="criterion"><h3>Criterion 22</h3><p>The provider is positioned to influence the scope and content of activities/ educational interventions.</p></article>
    </div>
    <p class="site">JRPPS URL http://www.jrpps.org</p>
  </section>
</main>
</body>
</html>
```